Teff Flour Bags

Need simple text, and a small design, in an "Ai File" to eventually be put on a plain brown bag 20lb. I need to send the "AI File" to a company, and they will do the printing onthe bags.

"TEFF FLOUR BROWN" please see uploaded file for samples

```html
<!DOCTYPE html>
<html lang="en">
<head>
<meta charset="utf-8">
<title>Teff Flour White – Bag Label</title>
<link href="https://fonts.googleapis.com/css2?family=Cormorant+Garamond:wght@600&family=EB+Garamond:wght@600;700&family=Noto+Serif+Ethiopic:wght@500&display=swap" rel="stylesheet">
<style>
  :root {
    --paper-light: #f1dfc3;
    --paper-mid: #ecd5b2;
    --paper-edge: #e3c8a2;
    --ink: #353333;
  }
  * { margin: 0; padding: 0; box-sizing: border-box; }
  html, body { width: 1200px; height: 1200px; overflow: hidden; }
  body {
    background: radial-gradient(ellipse at 55% 45%, var(--paper-light) 0%, var(--paper-mid) 60%, var(--paper-edge) 100%);
    color: var(--ink);
    font-family: "EB Garamond", Georgia, serif;
    position: relative;
  }
  .title { position: absolute; left: 0; top: 0; width: 1200px; height: 420px; }
  .title text { font-family: "Cormorant Garamond", Georgia, serif; font-weight: 600; fill: var(--ink); }
  .line {
    position: absolute; left: 0; width: 1200px; text-align: center;
    line-height: 1; white-space: nowrap;
  }
  .variety { top: 398px; font-size: 128px; font-weight: 600; letter-spacing: 1px; }
  .amharic { top: 560px; font-family: "Noto Serif Ethiopic", serif; font-size: 62px; font-weight: 500; }
  .french { top: 678px; font-size: 40px; font-weight: 700; }
  .weight { top: 746px; font-size: 56px; font-weight: 700; letter-spacing: 0.5px; }
  .company { top: 830px; font-size: 46px; font-weight: 700; letter-spacing: -0.5px; }
  .address { top: 908px; font-size: 42px; font-weight: 700; letter-spacing: -0.5px; }
  .city { top: 980px; font-size: 42px; font-weight: 700; letter-spacing: -0.5px; }
  .website { top: 1056px; font-size: 42px; font-weight: 700; }
</style>
</head>
<body>
  <svg class="title" viewBox="0 0 1200 420" aria-label="Teef Flour">
    <text textLength="912" lengthAdjust="spacingAndGlyphs" x="144">
      <tspan y="384" font-size="410">T</tspan><tspan y="372" font-size="360">E</tspan><tspan y="362" font-size="320">E</tspan><tspan y="352" font-size="280">F</tspan><tspan y="346" font-size="240"> </tspan><tspan y="344" font-size="236">F</tspan><tspan y="346" font-size="250">L</tspan><tspan y="352" font-size="290">O</tspan><tspan y="364" font-size="340">U</tspan><tspan y="384" font-size="400">R</tspan>
    </text>
  </svg>

  <div class="line variety">WHITE</div>
  <div class="line amharic" lang="am">ጥቁር ጤፍ ዱቄት</div>
  <div class="line french" lang="fr">FARINE DE TEFF</div>
  <div class="line weight">Net Weight 20 LBS. (9.09kg)</div>
  <div class="line company">Grainhaven Prairie Ltd.</div>
  <div class="line address">1207, 48th Ave N.E, Unit 12</div>
  <div class="line city">Red Deer, AB</div>
  <div class="line website">www.Grainhavenfoods.com</div>
</body>
</html>
```